TARPLOAD business card design

TARPLOAD is a manufacturer of skip bags supplying both the domestic and commercial market. We wish to convey core characteristics of strength, professionalism and reliability to our customers. We are after a business card that uses our company colours of black and yellow as well as incorporating our logo. Our customers are predominantly in the construction or hardware industry. It is important the cards are professional as we are a small company wishing to appear larger than we actually are. more info on the company and product available at www.tarpload-example.com.au

Target Market(s)

hardware buyers, contruction company owners

Industry/Entity Type

Construction

Requirements
Must have
• company colours of black and yellow - No other colours or variation of yellow black. our company logo. card design must convey "tough"
• Card design must be landscape
• Details to be included on the card are:
• Name and Tiltle
• Phone number : 1300 41 62 53
• Mobile: 0452 718 903
• Fax: 03 9617 4852
• email: dale.hendry@tarpload-example.com.au
• address: PO Box 517, Kelvindale, VIC,3294
• Text in white when on a black background
Nice to have
• I like the idea of the back of the card being black with lighter circle area in the middle with black logo in the centre. Similar to the attached "iconic" card

```html
<!DOCTYPE html>
<html lang="en">
<head>
<meta charset="utf-8">
<title>TARPLOAD business card</title>
<link href="https://fonts.googleapis.com/css2?family=Rubik:wght@400;500;700;800&display=swap" rel="stylesheet">
<style>
  :root {
    --stage: #8b8a89;
    --yellow-top: #e4952c;
    --yellow-bottom: #f3c20a;
    --ink: #231f20;
    --white: #ffffff;
    --grey-light: #c9c9c9;
    --grey-dark: #2f2f2f;
  }
  html, body {
    margin: 0;
    padding: 0;
    overflow: hidden;
  }
  .canvas {
    position: relative;
    width: 1200px;
    height: 943px;
    background: var(--stage);
    overflow: hidden;
    font-family: "Rubik", sans-serif;
  }
  .card-front {
    position: absolute;
    left: 279px;
    top: 153px;
    width: 258px;
    height: 394px;
    border-radius: 0 44px 0 44px;
    background: linear-gradient(160deg, var(--yellow-top) 0%, var(--yellow-bottom) 100%);
    color: var(--white);
    text-align: center;
  }
  .holder-name {
    position: absolute;
    top: 50px;
    left: 0;
    right: 0;
    font-size: 17px;
    font-weight: 700;
    letter-spacing: 0.2px;
  }
  .holder-title {
    position: absolute;
    top: 75px;
    left: 0;
    right: 0;
    display: flex;
    justify-content: center;
    align-items: center;
    gap: 5px;
    font-size: 7px;
    font-weight: 700;
    letter-spacing: 0.2px;
  }
  .holder-title::before,
  .holder-title::after {
    content: "";
    width: 13px;
    height: 1px;
    background: var(--white);
  }
  .brand-name {
    position: absolute;
    left: 0;
    right: 0;
    font-weight: 800;
    color: var(--ink);
    letter-spacing: 0.5px;
  }
  .card-front .brand-name {
    top: 188px;
    font-size: 24px;
  }
  .contact-box {
    position: absolute;
    left: 24px;
    top: 254px;
    width: 209px;
    height: 84px;
  }
  .contact-box svg {
    position: absolute;
    inset: 0;
  }
  .contact-list {
    position: relative;
    margin: 0;
    padding: 9px 0 0;
    list-style: none;
    font-size: 9.5px;
    line-height: 13px;
  }
  .contact-list .value {
    font-size: 8.3px;
  }
  .contact-list .email .value,
  .contact-list .address .value {
    font-size: 7.6px;
  }
  .card-back {
    position: absolute;
    left: 538px;
    top: 289px;
    width: 396px;
    height: 258px;
    border-radius: 44px 0 44px 0;
    background: radial-gradient(ellipse 60% 70% at 50% 50%, var(--grey-light) 0%, #8f8f8f 50%, var(--grey-dark) 100%);
  }
  .card-back .brand-name {
    top: 112px;
    font-size: 34px;
    text-align: center;
  }
</style>
</head>
<body>
  <main class="canvas">
    <section class="card-front" aria-label="Card front">
      <div class="holder-name">Dale Hendry</div>
      <div class="holder-title">MANAGING DIRECTOR</div>
      <div class="brand-name">TARPLOAD</div>
      <div class="contact-box">
        <svg width="209" height="84" viewBox="0 0 209 84" aria-hidden="true">
          <g fill="none" stroke="#ffffff" stroke-width="1.5">
            <path d="M33 1 H1 V83 H33"/>
            <path d="M176 1 H208 V83 H176"/>
          </g>
        </svg>
        <ul class="contact-list">
          <li>Phone number: <span class="value">1300 41 62 53</span></li>
          <li>Mobile: <span class="value">0452 718 903</span></li>
          <li>Fax: <span class="value">03 9617 4852</span></li>
          <li class="email">email: <span class="value">dale.hendry@tarpload-example.com.au</span></li>
          <li class="address">address: <span class="value">PO Box 517, Kelvindale, VIC,3294</span></li>
        </ul>
      </div>
    </section>
    <section class="card-back" aria-label="Card back">
      <div class="brand-name">TARPLOAD</div>
    </section>
  </main>
</body>
</html>
```